Varlow Business Partners
Business Cards & Stationery
Professional
Thomas E. Varlow
CEO
58 Birch Lane, North
Suite 318
Edgeton, NJ 07415
thomas.varlow@varlowbp.com
Back of card should contain the black version of the logo - no other information

```html
<!DOCTYPE html>
<html lang="en">
<head>
<meta charset="utf-8">
<title>Varlow Business Partners – Business Cards</title>
<link rel="stylesheet" href="https://fonts.googleapis.com/css2?family=Open+Sans:wght@400;600;700&display=swap">
<style>
  :root {
    --backdrop: #e9e6e1;
    --card-white: #ffffff;
    --ink-grey: #6d7075;
    --ink-dark: #4a4d52;
    --accent-orange: #e8621a;
    --band-light: #e4e5e7;
    --band-mid: #c9cbce;
    --band-dark: #a9acb0;
    --silver-light: #d9dbde;
    --silver-mid: #b8bbbf;
    --silver-dark: #9a9ea3;
    --logo-white: #ffffff;
  }
  * { box-sizing: border-box; margin: 0; padding: 0; }
  html, body {
    width: 1200px; height: 794px; overflow: hidden;
    background: var(--backdrop);
    font-family: "Open Sans", Arial, sans-serif;
  }
  .stage { position: relative; width: 1200px; height: 794px; }
  .card {
    position: absolute; width: 520px; height: 298px;
    border-radius: 18px; overflow: hidden;
    box-shadow: 0 6px 18px rgba(0,0,0,0.18);
  }
  .card-front { left: 80px; top: 100px; background: var(--card-white); }
  .card-back {
    left: 610px; top: 400px;
    background: linear-gradient(135deg, var(--silver-light) 0%, var(--silver-mid) 50%, var(--silver-dark) 100%);
  }
  .front-band { position: absolute; left: 0; top: 0; width: 520px; height: 298px; }

  .brand {
    position: absolute; display: flex; align-items: center; gap: 12px;
  }
  .brand-dot { border-radius: 50%; flex: none; }
  .brand-name { font-weight: 600; text-transform: uppercase; line-height: 1.15; letter-spacing: 0.02em; }

  .card-front .brand { left: 110px; top: 48px; }
  .card-front .brand-dot { width: 34px; height: 34px; background: var(--ink-grey); }
  .card-front .brand-name { color: var(--ink-grey); font-size: 19px; }

  .person { position: absolute; left: 150px; top: 136px; display: flex; align-items: baseline; gap: 18px; }
  .person-name { color: var(--accent-orange); font-weight: 700; font-size: 15px; }
  .person-title { color: var(--ink-grey); font-size: 11px; font-weight: 600; }

  .address {
    position: absolute; left: 62px; top: 222px;
    color: var(--ink-dark); font-size: 11px; line-height: 1.45;
  }
  .contacts {
    position: absolute; left: 278px; top: 208px; list-style: none;
    color: var(--ink-dark); font-size: 11px; line-height: 1.45;
  }
  .contacts li { display: flex; align-items: center; gap: 6px; }
  .contacts svg { width: 11px; height: 11px; flex: none; }

  .card-back .brand { left: 100px; top: 110px; }
  .card-back .brand-dot { width: 52px; height: 52px; background: var(--logo-white); }
  .card-back .brand-name { color: var(--logo-white); font-size: 28px; }
</style>
</head>
<body>
<main class="stage">
  <section class="card card-front" aria-label="Business card front">
    <svg class="front-band" viewBox="0 0 520 298" aria-hidden="true">
      <defs>
        <linearGradient id="bandGradient" x1="0" y1="0" x2="0" y2="1">
          <stop offset="0" stop-color="var(--band-light)"/>
          <stop offset="0.5" stop-color="var(--band-mid)"/>
          <stop offset="1" stop-color="var(--band-dark)"/>
        </linearGradient>
      </defs>
      <path d="M0 190 C150 150 330 150 520 175 L520 298 L0 298 Z" fill="url(#bandGradient)"/>
      <path d="M0 190 C150 150 330 150 520 175" fill="none" stroke="#ffffff" stroke-width="3"/>
    </svg>

    <div class="brand">
      <span class="brand-dot"></span>
      <span class="brand-name">Varlow<br>Business<br>Partners</span>
    </div>

    <div class="person">
      <span class="person-name">Thomas E. Varlow</span>
      <span class="person-title">CEO</span>
    </div>

    <address class="address" style="font-style:normal">
      58 Birch Lane, North<br>
      Suite 318 Edgeton, NJ 07415
    </address>

    <ul class="contacts">
      <li>
        <svg viewBox="0 0 12 12" aria-hidden="true"><circle cx="6" cy="6" r="6" fill="var(--ink-grey)"/><path d="M4 3 L5.2 3 L5.6 4.6 L4.9 5.2 C5.3 6.1 5.9 6.7 6.8 7.1 L7.4 6.4 L9 6.8 L9 8 C6 8.3 3.7 6 4 3 Z" fill="#fff"/></svg>
        <span>732.604.2185</span>
      </li>
      <li>
        <svg viewBox="0 0 12 12" aria-hidden="true"><circle cx="6" cy="6" r="6" fill="var(--ink-grey)"/><rect x="3" y="4" width="6" height="4.2" fill="#fff"/><path d="M3 4 L6 6.4 L9 4" fill="none" stroke="var(--ink-grey)" stroke-width="0.7"/></svg>
        <span>thomas.varlow@varlowbp.com</span>
      </li>
    </ul>
  </section>

  <section class="card card-back" aria-label="Business card back">
    <div class="brand">
      <span class="brand-dot"></span>
      <span class="brand-name">Varlow<br>Business Partners</span>
    </div>
  </section>
</main>
</body>
</html>
```